Business Card Design Project

Use our current logo. Clean design.

Industry/Entity Type

Business

Requirements
Must have
• Marisela DUCRANTE
M. Law
Managing Partner

Velotrana AG
Brunnmattweg 274
CH-3097 Liebefeld

M. +41 79 418 26 97
T. +41 31 742 19 04
F. +41 31 742 19 38

m.ducrante@velotrana.example
www.velotrana.example

```html
<!DOCTYPE html>
<html lang="en">
<head>
<meta charset="utf-8">
<title>Velotrana AG – Business Card</title>
<link rel="stylesheet" href="https://fonts.googleapis.com/css2?family=Rosario:wght@400&display=swap">
<style>
  :root {
    --ink: #111111;
    --accent: #e30613;
    --paper: #ffffff;
    --frame: #111111;
  }
  * { margin: 0; padding: 0; box-sizing: border-box; }
  html, body {
    width: 1200px;
    height: 1000px;
    overflow: hidden;
    background: var(--paper);
  }
  body {
    position: relative;
    font-family: "Rosario", sans-serif;
    color: var(--ink);
  }
  .card {
    position: absolute;
    left: 244px;
    width: 738px;
    height: 427px;
    border: 3px solid var(--frame);
    background: var(--paper);
  }
  .card--front { top: 44px; }
  .card--back { top: 509px; }

  .person {
    position: absolute;
    left: 53px;
    top: 50px;
  }
  .person__name { font-size: 36px; line-height: 1; }
  .person__degree { font-size: 34px; line-height: 1; margin-top: 24px; }
  .person__role { font-size: 24px; line-height: 1; margin-top: 20px; }

  .contact {
    position: absolute;
    left: 50px;
    top: 240px;
    list-style: none;
    font-size: 20px;
    line-height: 34px;
  }
  .contact li:last-child { line-height: 30px; }

  .divider-vertical {
    position: absolute;
    left: 420px;
    top: 41px;
    width: 3px;
    height: 345px;
    background: var(--accent);
  }

  .brand {
    position: absolute;
    left: 460px;
    width: 240px;
    text-align: center;
    font-size: 44px;
    line-height: 1;
    letter-spacing: 0.5px;
  }
  .card--front .brand { top: 160px; }

  .address {
    position: absolute;
    left: 460px;
    width: 240px;
    top: 258px;
    text-align: center;
    list-style: none;
    font-size: 20px;
    line-height: 34px;
  }

  .card--back .brand {
    left: 0;
    width: 100%;
    top: 170px;
    font-size: 66px;
  }
  .divider-horizontal {
    position: absolute;
    left: 0;
    right: 0;
    top: 337px;
    height: 3px;
    background: var(--accent);
  }
  .website {
    position: absolute;
    left: 0;
    width: 100%;
    top: 358px;
    text-align: center;
    font-size: 24px;
    line-height: 1;
  }
</style>
</head>
<body>
  <section class="card card--front">
    <div class="person">
      <p class="person__name">Marisela Ducrante</p>
      <p class="person__degree">M. Law</p>
      <p class="person__role">Managing Partner</p>
    </div>
    <ul class="contact">
      <li>M. +41 79 418 26 97</li>
      <li>T. +41 31 742 19 04</li>
      <li>F. +41 31 742 19 38</li>
      <li>E. m.ducrante@velotrana.example</li>
    </ul>
    <div class="divider-vertical"></div>
    <p class="brand">Velotrana</p>
    <ul class="address">
      <li>Velotrana AG</li>
      <li>Brunnmattweg 274</li>
      <li>CH-3097 Liebefeld</li>
    </ul>
  </section>

  <section class="card card--back">
    <p class="brand">Velotrana</p>
    <div class="divider-horizontal"></div>
    <p class="website">www.velotrana.example</p>
  </section>
</body>
</html>
```